cleaning service

we are a cleaning company,

we have a current flyer but its very dull

I have attached it, can we make it look modern, maybe add pictures and colour

```html
<!DOCTYPE html>
<html lang="en">
<head>
<meta charset="utf-8">
<title>One Off Deep Cleaning Service – Marla's Nest</title>
<link rel="stylesheet" href="https://fonts.googleapis.com/css2?family=Roboto+Condensed:wght@400;700&family=Arimo:wght@400&display=swap">
<style>
  :root {
    --brand-red: #8e1c1c;
    --ink: #111111;
    --body-ink: #2b2b2b;
    --cream: #fdf3e2;
    --band-light: #fdf0d2;
    --band-mid: #fde3a4;
    --sun: #fdc614;
    --sun-deep: #f9a51a;
  }
  * { margin: 0; padding: 0; box-sizing: border-box; }
  html, body { width: 849px; height: 1200px; overflow: hidden; }
  body {
    position: relative;
    background: linear-gradient(180deg, #ffffff 0%, #fffcf6 20%, var(--cream) 100%);
    font-family: "Arimo", Arial, sans-serif;
    color: var(--body-ink);
  }
  .heading-font { font-family: "Roboto Condensed", "Arial Narrow", sans-serif; }

  .corner-blob { position: absolute; }
  .corner-blob--top { top: 0; right: 0; width: 240px; height: 160px; }
  .corner-blob--bottom { left: 0; bottom: 0; width: 275px; height: 180px; }

  .hero-illustration {
    position: absolute; left: 668px; top: 10px; width: 160px; height: 175px;
    border-radius: 12px;
    background: linear-gradient(135deg, #e8403f 0%, #e8403f 30%, #3f6fa8 55%, #f2b21c 100%);
    opacity: 0.85;
  }

  .masthead {
    position: absolute; left: 85px; top: 57px;
    font-weight: 700; font-size: 20px; line-height: 24px; color: var(--ink);
  }
  .masthead .brand { color: var(--brand-red); }

  .service-badge {
    position: absolute; left: 85px; top: 285px; width: 103px; height: 103px;
    border: 1.2px solid var(--brand-red); border-radius: 50%;
  }

  .service-title {
    position: absolute; left: 85px; top: 410px;
    font-weight: 700; font-size: 25px; color: var(--brand-red);
  }

  .copy {
    position: absolute; white-space: nowrap;
    font-size: 17px; line-height: 22.9px; letter-spacing: 0.15px;
  }
  .copy--intro-left { left: 85px; top: 462px; }
  .copy--intro-right { left: 443px; top: 460px; }
  .copy--detail-left { left: 85px; top: 763px; }
  .copy--detail-right { left: 443px; top: 763px; }

  .price-band {
    position: absolute; left: 172px; top: 624px; width: 543px; height: 77px;
    border-radius: 22px;
    background: linear-gradient(90deg, var(--band-light) 0%, var(--band-mid) 100%);
    display: flex; align-items: center; justify-content: center;
    font-weight: 700; font-size: 22.5px; color: var(--ink);
  }
  .price-band .price { color: var(--brand-red); font-size: 30px; margin: 0 5px 0 10px; }

  .contact-strip {
    position: absolute; left: 383px; top: 1082px; width: 466px; height: 60px;
    border-radius: 30px 0 0 30px;
    background: linear-gradient(90deg, var(--cream) 0%, #fde9b0 60%, var(--sun-deep) 100%);
    padding: 10px 0 0 32px;
  }
  .contact-strip .note { font-weight: 700; font-size: 11.5px; color: var(--ink); }
  .contact-strip .call { font-weight: 700; font-size: 21.5px; color: var(--brand-red); line-height: 26px; }
</style>
</head>
<body>
  <svg class="corner-blob corner-blob--top" viewBox="0 0 240 160" aria-hidden="true">
    <path d="M50 0 H240 V160 C215 150 200 110 170 95 C130 75 70 90 50 45 C42 28 44 10 50 0 Z" fill="var(--sun)"/>
  </svg>

  <div class="hero-illustration" role="img" aria-label="Illustration of a cleaner in blue overalls steam-cleaning a red curtain with a yellow steamer"></div>

  <header class="masthead heading-font">
    <div>CLEANING SERVICES</div>
    <div>by <span class="brand">MARLA'S NEST</span></div>
  </header>

  <div class="service-badge" aria-hidden="true"></div>

  <h1 class="service-title heading-font">One Off Deep Cleaning Service</h1>

  <p class="copy copy--intro-left">If you require one-off cleaning to freshen<br>up your home Marla's Cleaning Services can<br>help you. We can arrange for a team of<br>professional cleaners to come to your</p>
  <p class="copy copy--intro-right">home at a time that's convenient for you.<br>Our deep cleaning service is perfect for all<br>households looking to save themselves<br>from tiresome home spring cleaning.</p>

  <div class="price-band heading-font">Including our cleaning materials <span class="price">£16</span> (per hour)</div>

  <p class="copy copy--detail-left">Our One-off service is a deep cleaning of<br>your home, rental flat, or holiday house in<br>London and the nearby towns. Marla's<br>Cleaning team can bring cleaning solutions<br>and equipment, or we can do the service<br>with tools and supplies provided by you.</p>
  <p class="copy copy--detail-right">We will work according to your<br>requirements, and you can create a<br>checklist with the areas you want us clean.<br>The service is perfect for your Spring<br>cleaning or any other general clean-up of<br>the house.</p>

  <svg class="corner-blob corner-blob--bottom" viewBox="0 0 275 180" aria-hidden="true">
    <defs>
      <linearGradient id="sunFade" x1="0" y1="0" x2="1" y2="1">
        <stop offset="0" stop-color="var(--sun)"/>
        <stop offset="1" stop-color="var(--sun-deep)"/>
      </linearGradient>
    </defs>
    <path d="M0 0 C15 10 18 50 35 75 C60 110 110 95 150 120 C190 140 200 165 215 180 H0 Z" fill="url(#sunFade)"/>
  </svg>

  <div class="contact-strip heading-font">
    <div class="note">Please turnover for our services and prices</div>
    <div class="call">Please call us on 07700900123 to beat any price</div>
  </div>
</body>
</html>
```